Design for an iOS and Android app managing shopping list

The app allows you to keep manage shopping lists, each shopping list being made of items to buy...
We need a design for the 3 screens of the app:
a) global view showing list of (shopping) list
b) form enabling to edit the name of a (shopping) list
c) detailed view listing the contents/items of a (shopping) list
d) 1 text page [not illustrated]
2 "alerts" items are also to be designed: confirm and error pop ups.
No specific guidelines, nor logo or whatever.
It will be a free app distributed on iOS and Androïd.
We just want to make it looking nice & very usable for end users.

```html
<!DOCTYPE html>
<html lang="en">
<head>
<meta charset="utf-8">
<title>Shopping List – Confirm Pop-Up</title>
<link href="https://fonts.googleapis.com/css2?family=Lato:wght@300;400&family=Mukta:wght@400;600;700&display=swap" rel="stylesheet">
<style>
  :root {
    --stage: #f34d3b;
    --header: #d8342a;
    --pending: #2f9fd8;
    --done: #1fb07a;
    --row-bg: #ffffff;
    --row-line: #e3e3e3;
    --ink: #222222;
    --muted: #777777;
    --danger: #d9303e;
    --accent-red: #e0392e;
    --confirm: #1dd08c;
    --icon-blue: #1c76c5;
    --dim: rgba(0, 0, 0, 0.5);
    --white: #ffffff;
  }
  * { box-sizing: border-box; margin: 0; padding: 0; }
  html, body { width: 1200px; height: 675px; overflow: hidden; }
  body {
    background: var(--stage);
    font-family: "Mukta", "Segoe UI", sans-serif;
    position: relative;
  }
  .screen {
    position: absolute;
    left: 133px; top: 176px;
    width: 279px; height: 499px;
    background: var(--row-bg);
    overflow: hidden;
  }
  .status-bar {
    height: 13px; background: var(--header);
    display: flex; align-items: center; justify-content: space-between;
    padding: 0 6px; color: var(--white); font-size: 7px; font-weight: 600;
  }
  .app-header {
    height: 44px; background: var(--header);
    display: flex; align-items: center; padding: 0 10px; color: var(--white);
  }
  .app-header .back { width: 14px; }
  .app-header .title { flex: 1; font-size: 17px; font-weight: 700; margin-left: 10px; }
  .new-item {
    height: 38px; display: flex; align-items: center; padding: 0 12px;
  }
  .new-item .field {
    flex: 1; border-bottom: 1px solid #999; font-size: 8.5px; color: var(--muted);
    padding-bottom: 1px; margin-right: 14px;
  }
  .section {
    height: 25px; display: flex; align-items: center; justify-content: center;
    color: var(--white); font-size: 11px; font-weight: 600;
  }
  .section.pending { background: var(--pending); }
  .section.done { background: var(--done); }
  .item {
    height: 40px; display: flex; align-items: center; padding: 0 10px;
    border-bottom: 1px solid var(--row-line); font-size: 11px; font-weight: 700; color: var(--ink);
  }
  .item.completed { border-left: 3px solid var(--accent-red); padding-left: 7px; }
  .item .check {
    width: 18px; height: 18px; border-radius: 50%; border: 1.3px solid #555;
    margin-right: 8px; flex: none; display: flex; align-items: center; justify-content: center;
  }
  .item .name { flex: 1; }
  .dim { position: absolute; inset: 0; background: var(--dim); }
  .dialog {
    position: absolute; left: 39px; top: 153px; width: 201px; height: 191px;
    background: var(--white); border-radius: 8px;
    display: flex; flex-direction: column; align-items: center; text-align: center;
    padding-top: 27px;
  }
  .dialog h2 { font-size: 11.5px; font-weight: 700; color: var(--ink); margin-top: 15px; line-height: 1.2; }
  .dialog p { font-size: 8px; color: var(--ink); margin-top: 4px; }
  .dialog .actions { display: flex; gap: 7px; margin-top: 23px; }
  .btn {
    width: 55px; height: 21px; border-radius: 3px; color: var(--white);
    font-size: 8.5px; font-weight: 700; display: flex; align-items: center; justify-content: center;
  }
  .btn.cancel { background: var(--confirm); }
  .btn.delete { background: var(--danger); }
  .caption {
    position: absolute; left: 487px; top: 355px;
    font-family: "Lato", sans-serif; font-weight: 300; font-size: 33px; color: var(--white);
  }
</style>
</head>
<body>
  <div class="screen">
    <div class="status-bar"><span>▪▪▪▪ LM CZ</span><span>2:49 PM</span><span>41 %</span></div>
    <div class="app-header">
      <svg class="back" viewBox="0 0 14 22" width="10" height="18"><path d="M12 2 3 11l9 9" fill="none" stroke="#fff" stroke-width="2"/></svg>
      <span class="title">Diner de ce soir</span>
      <svg viewBox="0 0 24 20" width="21" height="18"><path d="M2 7h20l-2.5 11h-15zM7 7l5-6 5 6M9 10v6M12 10v6M15 10v6" fill="none" stroke="#fff" stroke-width="1.6"/></svg>
    </div>
    <div class="new-item">
      <span class="field">Add a new Item</span>
      <svg viewBox="0 0 16 16" width="15" height="15"><circle cx="8" cy="8" r="8" fill="#222"/><path d="M8 4v8M4 8h8" stroke="#fff" stroke-width="1.8"/></svg>
    </div>
    <div class="section pending">Pending Items</div>
    <div class="item"><span class="check"></span><span class="name">Diner de ce soir</span><svg viewBox="0 0 14 16" width="14" height="16"><path d="M1 3h12M5 3V1h4v2M2.5 3l1 12h7l1-12M5.5 6v7M8.5 6v7" fill="none" stroke="#e0392e" stroke-width="1.5"/></svg></div>
    <div class="item"><span class="check"></span><span class="name">Diner de ce soir</span><svg viewBox="0 0 14 16" width="14" height="16"><path d="M1 3h12M5 3V1h4v2M2.5 3l1 12h7l1-12M5.5 6v7M8.5 6v7" fill="none" stroke="#e0392e" stroke-width="1.5"/></svg></div>
    <div class="item"><span class="check"></span><span class="name">Diner de ce soir</span><svg viewBox="0 0 14 16" width="14" height="16"><path d="M1 3h12M5 3V1h4v2M2.5 3l1 12h7l1-12M5.5 6v7M8.5 6v7" fill="none" stroke="#e0392e" stroke-width="1.5"/></svg></div>
    <div class="item"><span class="check"></span><span class="name">Diner de ce soir</span><svg viewBox="0 0 14 16" width="14" height="16"><path d="M1 3h12M5 3V1h4v2M2.5 3l1 12h7l1-12M5.5 6v7M8.5 6v7" fill="none" stroke="#e0392e" stroke-width="1.5"/></svg></div>
    <div class="section done">Completed Items</div>
    <div class="item completed"><span class="check"><svg viewBox="0 0 10 8" width="9" height="7"><path d="M1 4l3 3 5-6" fill="none" stroke="#222" stroke-width="1.4"/></svg></span><span class="name">Diner de ce soir</span><svg viewBox="0 0 14 16" width="14" height="16"><path d="M1 3h12M5 3V1h4v2M2.5 3l1 12h7l1-12M5.5 6v7M8.5 6v7" fill="none" stroke="#e0392e" stroke-width="1.5"/></svg></div>
    <div class="item completed"><span class="check"><svg viewBox="0 0 10 8" width="9" height="7"><path d="M1 4l3 3 5-6" fill="none" stroke="#222" stroke-width="1.4"/></svg></span><span class="name">Diner de ce soir</span><svg viewBox="0 0 14 16" width="14" height="16"><path d="M1 3h12M5 3V1h4v2M2.5 3l1 12h7l1-12M5.5 6v7M8.5 6v7" fill="none" stroke="#e0392e" stroke-width="1.5"/></svg></div>
    <div class="item completed"><span class="check"><svg viewBox="0 0 10 8" width="9" height="7"><path d="M1 4l3 3 5-6" fill="none" stroke="#222" stroke-width="1.4"/></svg></span><span class="name">Diner de ce soir</span><svg viewBox="0 0 14 16" width="14" height="16"><path d="M1 3h12M5 3V1h4v2M2.5 3l1 12h7l1-12M5.5 6v7M8.5 6v7" fill="none" stroke="#e0392e" stroke-width="1.5"/></svg></div>
    <div class="item completed"><span class="check"><svg viewBox="0 0 10 8" width="9" height="7"><path d="M1 4l3 3 5-6" fill="none" stroke="#222" stroke-width="1.4"/></svg></span><span class="name">Diner de ce soir</span><svg viewBox="0 0 14 16" width="14" height="16"><path d="M1 3h12M5 3V1h4v2M2.5 3l1 12h7l1-12M5.5 6v7M8.5 6v7" fill="none" stroke="#e0392e" stroke-width="1.5"/></svg></div>
    <div class="item completed"><span class="check"><svg viewBox="0 0 10 8" width="9" height="7"><path d="M1 4l3 3 5-6" fill="none" stroke="#222" stroke-width="1.4"/></svg></span><span class="name">Diner de ce soir</span><svg viewBox="0 0 14 16" width="14" height="16"><path d="M1 3h12M5 3V1h4v2M2.5 3l1 12h7l1-12M5.5 6v7M8.5 6v7" fill="none" stroke="#e0392e" stroke-width="1.5"/></svg></div>

    <div class="dim"></div>

    <div class="dialog" role="alertdialog" aria-label="Remove Shopping List">
      <svg viewBox="0 0 52 52" width="50" height="50" aria-hidden="true">
        <rect x="16" y="3" width="16" height="5" rx="2" fill="#1c76c5" transform="rotate(8 24 6)"/>
        <rect x="10" y="8" width="32" height="6" rx="2" fill="#1c76c5" transform="rotate(8 26 11)"/>
        <path d="M13 17h26l-3 33H16z" fill="#1c76c5"/>
        <path d="M21 22v23M26 22v23M31 22v23" stroke="#fff" stroke-width="2.5"/>
        <path d="M11 26C4 24 2 31 1 38 5 32 9 30 13 30" fill="#1c76c5"/>
        <path d="M9 22l7 4-6 5z" fill="#1c76c5"/>
      </svg>
      <h2>Remove Shopping List</h2>
      <p>Would you like to delete the Shopping list?</p>
      <div class="actions">
        <span class="btn cancel">CANCEL</span>
        <span class="btn delete">DELETE</span>
      </div>
    </div>
  </div>

  <div class="caption">Confirm Pop-Up</div>
</body>
</html>
```